Drawing Book Cover

I need a design for my Drawing Book which selling to Primary School and Secondary children. Following are the size and description.

Size: 15" x 11" (381mm x 280mm) Landscape.
I would like to see designs that use Black color only as the book cover will using Kraft Paper.

School

```html
<!DOCTYPE html>
<html lang="en">
<head>
<meta charset="utf-8">
<title>My Drawing Book – Cover</title>
<link rel="stylesheet" href="https://fonts.googleapis.com/css2?family=Cabin+Sketch:wght@700&display=swap">
<style>
  :root {
    --kraft-light: #d2b386;
    --kraft-mid: #c3a273;
    --kraft-dark: #a98a5e;
    --ink: #1d1812;
    --pencil-light: #e6d2ac;
    --pencil-mid: #b08d5f;
    --pencil-dark: #5a4128;
    --palette-light: #ecd9b5;
    --palette-dark: #9c7a4c;
  }
  * { margin: 0; padding: 0; box-sizing: border-box; }
  html, body {
    width: 1200px;
    height: 880px;
    overflow: hidden;
  }
  .cover {
    position: relative;
    width: 1200px;
    height: 880px;
    overflow: hidden;
    background:
      radial-gradient(ellipse at 50% 50%, var(--kraft-light) 0%, var(--kraft-mid) 60%, var(--kraft-dark) 100%);
  }
  .pencil-row {
    position: absolute;
    left: 0;
    width: 1200px;
    height: 125px;
  }
  .pencil-row--top { top: 0; }
  .pencil-row--bottom { bottom: 0; }
  .paint-palette {
    position: absolute;
    left: 768px;
    top: 174px;
    width: 252px;
    height: 294px;
  }
  .cover-title {
    position: absolute;
    left: 0;
    top: 270px;
    width: 1200px;
    font-family: "Cabin Sketch", cursive;
    font-weight: 700;
    color: var(--ink);
    line-height: 1;
  }
  .cover-title__small {
    display: block;
    position: absolute;
    left: 458px;
    top: 0;
    font-size: 180px;
    letter-spacing: 2px;
  }
  .cover-title__main {
    display: block;
    position: absolute;
    left: 236px;
    top: 176px;
    font-size: 108px;
    letter-spacing: 3px;
    white-space: nowrap;
  }
</style>
</head>
<body>
  <main class="cover">
    <svg class="pencil-row pencil-row--top" viewBox="0 0 1200 125" role="img" aria-label="Row of coloured pencils pointing down, in sepia tones">
      <defs>
        <linearGradient id="pencilTop" x1="0" y1="0" x2="0" y2="1">
          <stop offset="0" stop-color="var(--pencil-dark)"/>
          <stop offset="0.55" stop-color="var(--pencil-mid)"/>
          <stop offset="1" stop-color="var(--pencil-light)"/>
        </linearGradient>
      </defs>
      <rect width="1200" height="125" fill="url(#pencilTop)"/>
    </svg>

    <svg class="paint-palette" viewBox="0 0 252 294" role="img" aria-label="Wooden paint palette with two brushes">
      <defs>
        <radialGradient id="paletteTone" cx="0.45" cy="0.45" r="0.6">
          <stop offset="0" stop-color="var(--palette-light)"/>
          <stop offset="1" stop-color="var(--palette-dark)"/>
        </radialGradient>
      </defs>
      <ellipse cx="126" cy="160" rx="120" ry="110" fill="url(#paletteTone)"/>
    </svg>

    <h1 class="cover-title">
      <span class="cover-title__small">my</span>
      <span class="cover-title__main">Drawing Book</span>
    </h1>

    <svg class="pencil-row pencil-row--bottom" viewBox="0 0 1200 125" role="img" aria-label="Row of coloured pencils pointing up, in sepia tones">
      <defs>
        <linearGradient id="pencilBottom" x1="0" y1="1" x2="0" y2="0">
          <stop offset="0" stop-color="var(--pencil-dark)"/>
          <stop offset="0.55" stop-color="var(--pencil-mid)"/>
          <stop offset="1" stop-color="var(--pencil-light)"/>
        </linearGradient>
      </defs>
      <rect width="1200" height="125" fill="url(#pencilBottom)"/>
    </svg>
  </main>
</body>
</html>
```